bluegum voyages

We provide boar charter for :Fishing/whale watching and diving in Sydney Harbour providing for 12 passengersI have yet to have web page made but want to make logo first then do web page later. So I want to be able to edit and add this site to card later

Contact Information for Business Card

Captain Len (Doc) Wigellphone no 0457710098email awigell4@gmail.comCompany name Marlow Outings Pty Ltd in association with far reef cruises

Font styles to use
Serif

Requirements
Nice to have
• perhaps a photo of boat and some stick diagrams of fishing.whales and diviving

```html
<!DOCTYPE html>
<html lang="en">
<head>
<meta charset="utf-8">
<title>Marlow Outings Pty Ltd – Business Card</title>
<link rel="stylesheet" href="https://fonts.googleapis.com/css2?family=Roboto:wght@400;700&family=Tinos&display=swap">
<style>
  :root {
    --page: #eceff1;
    --card: #ffffff;
    --brand-blue: #2580fc;
    --photo-light: #eef4f8;
    --photo-mid: #d7e4ee;
    --text-light: #ffffff;
  }
  * { margin: 0; padding: 0; box-sizing: border-box; }
  html, body {
    width: 1200px; height: 1000px; overflow: hidden;
    background: var(--page);
  }
  .canvas { position: relative; width: 1200px; height: 1000px; }
  .card {
    position: absolute; width: 500px; height: 286px;
    background: var(--card);
    box-shadow: 0 6px 18px rgba(0,0,0,0.12);
    overflow: hidden;
  }
  .card--front { left: 70px; top: 357px; }
  .card--back { left: 630px; top: 357px; }

  /* Front */
  .front-band {
    position: absolute; left: 0; top: 0; width: 100%; height: 130px;
    background: var(--brand-blue);
  }
  .front-band__step {
    position: absolute; left: 330px; top: 130px; width: 170px; height: 60px;
    background: var(--brand-blue);
  }
  .brand-mark {
    position: absolute; left: 65px; top: 60px; width: 130px; height: 130px;
  }
  .brand-name {
    position: absolute; left: 10px; top: 198px; width: 240px;
    font-family: "Tinos", serif; font-size: 27px; line-height: 1.05;
    color: var(--brand-blue); text-align: center;
  }
  .contact {
    position: absolute; left: 250px; top: 30px;
    font-family: "Roboto", sans-serif; color: var(--text-light);
  }
  .contact__name { font-size: 22px; font-weight: 700; margin-bottom: 10px; }
  .contact__line {
    display: flex; align-items: center; gap: 8px;
    font-size: 14px; margin-bottom: 6px;
  }
  .contact__line svg { width: 14px; height: 14px; flex: none; }

  /* Back */
  .back-photo {
    position: absolute; inset: 0;
    background: linear-gradient(180deg, var(--photo-light) 0%, var(--photo-mid) 55%, var(--photo-light) 100%);
  }
  .back-mark {
    position: absolute; left: 185px; top: 35px; width: 130px; height: 130px;
  }
  .back-name {
    position: absolute; left: 0; top: 178px; width: 100%;
    font-family: "Tinos", serif; font-size: 27px; line-height: 1.05;
    color: var(--brand-blue); text-align: center;
  }
</style>
</head>
<body>
<main class="canvas">
  <section class="card card--front" aria-label="Business card front">
    <div class="front-band"></div>
    <div class="front-band__step"></div>
    <svg class="brand-mark" viewBox="0 0 130 130" aria-hidden="true">
      <circle cx="65" cy="65" r="59" fill="var(--card)" stroke="var(--brand-blue)" stroke-width="9"/>
    </svg>
    <div class="contact">
      <p class="contact__name">Captain Len</p>
      <p class="contact__line">
        <svg viewBox="0 0 16 16" aria-hidden="true"><circle cx="8" cy="8" r="7.5" fill="var(--text-light)"/><path d="M5 4.5l1.6-.4.8 2-1 .8a6 6 0 0 0 2.7 2.7l.8-1 2 .8-.4 1.6c-3.5.2-6.7-3-6.5-6.5z" fill="var(--brand-blue)"/></svg>
        0468 23 1594
      </p>
      <p class="contact__line">
        <svg viewBox="0 0 16 16" aria-hidden="true"><rect x="1" y="3" width="14" height="10" fill="var(--text-light)"/><path d="M1 3l7 5 7-5" fill="none" stroke="var(--brand-blue)" stroke-width="1.2"/></svg>
        lpruntel7@tidewake.net
      </p>
    </div>
    <p class="brand-name">Marlow Outings<br>Pty Ltd</p>
  </section>

  <section class="card card--back" aria-label="Business card back">
    <div class="back-photo" role="img" aria-label="Faded photograph of the charter boat on the harbour"></div>
    <svg class="back-mark" viewBox="0 0 130 130" aria-hidden="true">
      <circle cx="65" cy="65" r="59" fill="var(--card)" stroke="var(--brand-blue)" stroke-width="9"/>
    </svg>
    <p class="back-name">Marlow Outings<br>Pty Ltd</p>
  </section>
</main>
</body>
</html>
```